Brantley Advisory Group provides support for renewable energy projects to utilities and suppliers

I need a professional looking business card that is both simple and elegant and unique. My clients are mostly large organizations not individuals. I am a consultant with my own company that is small but would like to give clients the impression I am larger. Smart grid, fiber optics, software, field hardware, distribution automation, substation automation, operations, energy storage/batteries, microgrids, customer service, strategy/roadmaps, conservation, Automated Metering Infrastruture (AMI or smart meters) are all areas of focus.

Target Market(s)

Utilities, suppliers, governmental agencies involved in energy. All types of energy especially natural gas and electrical. Especially renewable energy or green projects.

Contact Information for Business Card

Name - Mark Brantley Cell Phone - 425.318.2746 Email - mbrantley@brantleyag-example.com
Company - Brantley Advisory Group (logo) Title - Principal

Font styles to use
Serif
Sans Serif

Colors

Designer to choose colors to be used in the design.

Requirements
Must have
• Simple and professional and powerful.
• Unique/creative design.
Nice to have
• Utilize color scheme to accent logo colors. Maybe some geometric pattern on edge of card with color.
Should not have
• Busy, complicated, traditional

```html
<!DOCTYPE html>
<html lang="en">
<head>
<meta charset="utf-8">
<title>Brantley Advisory Group — Business Card</title>
<link rel="stylesheet" href="https://fonts.googleapis.com/css2?family=Open+Sans:wght@400;600&display=swap">
<style>
  :root {
    --backdrop: #a9a9a9;
    --card: #ffffff;
    --navy: #1c1c9c;
    --ink: #222222;
    --frame-grey: #a0a0a0;
  }
  * { margin: 0; padding: 0; box-sizing: border-box; }
  html, body { width: 1200px; height: 1200px; overflow: hidden; }
  body {
    background: var(--backdrop);
    font-family: "Open Sans", Arial, sans-serif;
    position: relative;
  }
  .card {
    position: absolute;
    background: var(--card);
    border-radius: 48px;
  }
  .card--front { left: 186px; top: 115px; width: 841px; height: 465px; }
  .card--back  { left: 188px; top: 649px; width: 843px; height: 467px; }

  .brand {
    position: absolute;
    display: flex;
    align-items: center;
    gap: 22px;
    color: var(--navy);
    font-weight: 600;
  }
  .brand__square {
    border: 5px solid var(--navy);
    flex: none;
  }
  .brand__name { line-height: 1.05; }
  .brand__name span { display: block; }

  .card--front .brand { left: 236px; top: 160px; }
  .card--front .brand__square { width: 62px; height: 62px; }
  .card--front .brand__name span:first-child { font-size: 68px; letter-spacing: 0.5px; }
  .card--front .brand__name span:last-child { font-size: 37px; }

  .card--back .brand { left: 108px; top: 175px; gap: 14px; }
  .card--back .brand__square { width: 38px; height: 38px; border-width: 3px; }
  .card--back .brand__name span:first-child { font-size: 40px; }
  .card--back .brand__name span:last-child { font-size: 22px; }

  .divider {
    position: absolute;
    left: 449px; top: 109px;
    width: 2px; height: 248px;
    background: var(--navy);
  }
  .person { position: absolute; left: 463px; top: 132px; }
  .person__name { font-size: 34px; font-weight: 400; color: var(--navy); line-height: 1.2; }
  .person__title { font-size: 19px; color: var(--ink); margin-top: 4px; margin-left: 3px; }

  .contact { position: absolute; left: 463px; top: 264px; list-style: none; }
  .contact__item {
    display: flex; align-items: center; gap: 16px;
    font-size: 17px; color: var(--ink); height: 38px;
  }
  .contact__icon { width: 26px; height: 26px; flex: none; }
</style>
</head>
<body>
  <section class="card card--front">
    <div class="brand">
      <div class="brand__square"></div>
      <div class="brand__name"><span>Brantley</span><span>Advisory Group</span></div>
    </div>
  </section>

  <section class="card card--back">
    <div class="brand">
      <div class="brand__square"></div>
      <div class="brand__name"><span>Brantley</span><span>Advisory Group</span></div>
    </div>
    <div class="divider"></div>
    <div class="person">
      <p class="person__name">Mark Brantley</p>
      <p class="person__title">Principal</p>
    </div>
    <ul class="contact">
      <li class="contact__item">
        <svg class="contact__icon" viewBox="0 0 26 26" aria-hidden="true">
          <circle cx="13" cy="13" r="12" fill="#1c1c9c"/>
          <path d="M9 7c1 0 1.5 2.5 2 3.2.3.6-.8 1.3-.6 1.9.6 1.6 1.8 2.9 3.4 3.5.6.2 1.3-.9 1.9-.6.7.4 3.2 1 3.2 2 0 1.2-1.6 2-2.6 2C11 19 7 15 7 9.6 7 8.6 7.8 7 9 7z" fill="#fff"/>
        </svg>
        <span>425.318.2746</span>
      </li>
      <li class="contact__item">
        <svg class="contact__icon" viewBox="0 0 26 26" aria-hidden="true">
          <rect x="2" y="7" width="22" height="13" fill="#1c1c9c"/>
          <path d="M2 7l11 8 11-8" fill="none" stroke="#fff" stroke-width="1.5"/>
        </svg>
        <span>mbrantley@brantleyag-example.com</span>
      </li>
    </ul>
  </section>
</body>
</html>
```